Brimvale Solutions Website Project

We require a design to revamp and existing website for a company that provides online solutions for small the medium sized businesses including web development, online marketing, social media, online business plans, social media and e-commerce. We are looking to use colours that integrate well with the current logo. Our target market are small to medium sized businesses and individuals looking for a trusted adviser to cover all their online services.
Existing website - www.brimvalesolutions.com.au
Updates
Participation payments added.
Storyboard layout mentioned in brief was not attached in error. It will be uploaded shortly.
Storyboard file added.
Target Market(s)
Revamp of existing website - Looking for a professional design in line with the target market of small to medium businesses
Industry/Entity Type
Business
Requirements
Must have
- Refer the attached storyboard layout for the site design and requirements. Basic header, footer and sidebar are to be the same on every page with the content changing to match the requirements on each page. 8 pages in total
Should not have
- No click here text

```html
<!DOCTYPE html>
<html lang="en">
<head>
<meta charset="utf-8">
<title>Brimvale Solutions</title>
<link href="https://fonts.googleapis.com/css2?family=Open+Sans:wght@400;600;700&family=Noto+Serif:wght@700&display=swap" rel="stylesheet">
<style>
:root{
  --green:#5cb82c;
  --green-dark:#3f8f1a;
  --ink:#2b2b2b;
  --text:#444;
  --muted:#777;
  --page:#e6e6e6;
  --panel:#ffffff;
  --hero:#25343b;
  --footer:#2a2a2a;
  --footer-deep:#1b1b1b;
  --line:#d4d4d4;
}
*{box-sizing:border-box;margin:0;padding:0}
html,body{width:880px;height:1200px;overflow:hidden}
body{background:var(--page);font-family:"Open Sans",Arial,sans-serif;color:var(--text);font-size:11px;position:relative}
.abs{position:absolute}

/* top bar */
.topbar{left:0;top:0;width:880px;height:30px;background:#fff}
.topbar .contact{right:120px;top:8px;font-size:10px;color:var(--text)}
.topbar .contact b{color:var(--green)}
.topbar .follow{right:30px;top:26px;font-size:11px;color:var(--green);font-weight:700}
.topbar .follow i{display:inline-block;width:12px;height:12px;background:var(--green);border-radius:2px;margin-left:4px;vertical-align:middle}

/* header */
.header{left:0;top:30px;width:880px;height:80px;background:#fff}
.brand{left:34px;top:10px;display:flex;align-items:center;gap:10px}
.brand .mark{width:54px;height:54px;border-radius:50%;background:var(--green)}
.brand .name{font-size:22px;font-weight:700;color:var(--ink);line-height:1}
.nav{left:456px;top:46px;width:394px;height:34px;background:var(--green);border-radius:6px 6px 0 0;display:flex;align-items:center;justify-content:space-around;padding:0 8px}
.nav a{color:#fff;text-decoration:none;font-size:12px;font-weight:600;padding:6px 10px}
.nav a.active{background:var(--ink);border-radius:3px}

/* hero */
.hero{left:30px;top:118px;width:820px;height:236px;background:var(--hero);border:5px solid #cfcfcf}
.hero .photo{left:0;top:0;width:240px;height:226px;background:linear-gradient(135deg,#f1ece4,#c9c3b8)}
.hero .tagline{left:260px;top:50px;width:270px;color:#fff;font-size:22px;line-height:1.2;font-weight:600}
.hero .cta{left:260px;top:140px;color:#fff;font-size:17px;line-height:1.25}
.hero .cta span{color:var(--green);font-weight:700}
.quote{left:560px;top:-5px;width:258px;height:236px;background:var(--green);padding:12px 16px}
.quote h2{color:#fff;font-size:15px;text-align:center;margin-bottom:8px}
.quote .field{background:#fff;height:20px;margin-bottom:6px;font-size:10px;color:var(--muted);padding:3px 6px}
.quote .field.msg{height:58px}
.quote .submit{float:right;background:var(--ink);color:#fff;font-size:11px;padding:4px 16px;border-radius:3px}

/* services */
.services{left:30px;top:364px;width:820px;height:262px;background:#f2f2f2;border:1px solid var(--line)}
.service{width:250px;height:118px}
.service .icon{left:0;top:4px;width:60px;height:60px;border-radius:50%;background:radial-gradient(circle,#f4c14d,#d97c1e)}
.service h3{left:72px;top:2px;font-size:11px;font-weight:700;color:var(--ink)}
.service p{left:72px;top:20px;width:178px;font-size:9.5px;line-height:1.35;color:var(--muted)}
.more{background:#fff;border:1px solid var(--line);color:var(--ink);font-size:9px;font-weight:700;padding:3px 10px}

/* recent work */
.recent{left:30px;top:630px;width:820px;height:144px}
.recent h2,.why h2{font-family:"Noto Serif",Georgia,serif;font-size:13px;color:var(--ink)}
.strip{left:0;top:22px;width:820px;height:114px;background:#fff;border:1px solid var(--line)}
.arrow{top:46px;width:0;height:0;border-top:10px solid transparent;border-bottom:10px solid transparent}
.arrow.l{left:6px;border-right:12px solid #999}
.arrow.r{right:6px;border-left:12px solid #999}
.thumb{top:10px;width:116px;height:92px;background:linear-gradient(#fafafa,#dcdcdc);border:1px solid var(--line);box-shadow:0 2px 3px rgba(0,0,0,.15)}

/* why choose us */
.why{left:30px;top:782px;width:820px;height:232px}
.why .body{left:0;top:20px;width:520px;height:204px;border-top:2px solid var(--green)}
.why ul{list-style:none;font-size:10px;line-height:2.1;color:var(--text)}
.why li::before{content:"";display:inline-block;width:6px;height:6px;background:var(--green);border-radius:50%;margin-right:6px;vertical-align:middle}
.why .more-link{right:0;top:174px;font-size:10px;font-weight:700;color:var(--green)}
.feed{left:548px;top:0;width:272px;height:138px;background:#fff;border:1px solid var(--line)}
.feed h3{background:var(--ink);color:#fff;font-size:11px;padding:6px 10px}
.feed p{font-size:9.5px;line-height:1.35;color:var(--muted);padding:6px 10px 0}
.feed .time{color:var(--green);font-weight:700}
.fbox{left:548px;top:146px;width:272px;height:80px;background:#fff;border:1px solid var(--line);display:flex;align-items:center;gap:10px;padding:10px}
.fbox .mark{width:46px;height:46px;border-radius:50%;background:var(--green)}
.fbox .name{font-size:13px;font-weight:700;color:var(--ink);line-height:1.2}
.fbox .on{font-size:9px;color:var(--muted);font-weight:700}

/* footer */
.footer{left:0;top:1020px;width:880px;height:150px;background:var(--footer)}
.footer h4{color:#fff;font-size:13px;font-weight:600;margin-bottom:8px}
.footer .col{top:14px;color:#cfcfcf;font-size:9.5px;line-height:1.6}
.footer .links{display:grid;grid-template-columns:76px 90px}
.footer .when{color:var(--green);font-weight:700}
.footer .soc{display:flex;align-items:center;gap:8px;margin-bottom:6px}
.footer .soc i{width:14px;height:14px;background:var(--green);border-radius:2px}
.copy{left:0;top:1170px;width:880px;height:30px;background:var(--footer-deep);color:#aaa;font-size:9px;text-align:right;padding:9px 30px}
</style>
</head>
<body>

<div class="abs topbar">
  <div class="abs contact"><b>email:</b> contact@brimvalesolutions.com.au &nbsp;&nbsp; <b>call:</b> 0400 123 456</div>
  <div class="abs follow">Follow us <i></i><i></i></div>
</div>

<header class="abs header">
  <div class="abs brand"><div class="mark"></div><div class="name">Brimvale Solutions</div></div>
  <nav class="abs nav">
    <a class="active">Home</a><a>About</a><a>Services</a><a>Portfolio</a><a>Contact</a>
  </nav>
</header>

<section class="abs hero">
  <div class="abs photo" role="img" aria-label="Photo of a smiling professional working at a laptop"></div>
  <div class="abs tagline">Brimvale Solutions provide superior online solutions</div>
  <div class="abs cta"><span>Contact us →</span><br>to discuss your project.</div>
  <form class="abs quote">
    <h2>Request a quote</h2>
    <div class="field">Name</div>
    <div class="field">Email</div>
    <div class="field">Phone</div>
    <div class="field msg">Message</div>
    <div class="submit">Submit</div>
  </form>
</section>

<section class="abs services">
  <div class="abs service" style="left:20px;top:18px">
    <div class="abs icon" role="img" aria-label="Blog icon"></div>
    <h3 class="abs">BLOGS</h3>
    <p class="abs">Need a dynamic blog to complement your business or want a blog for personal expression?</p>
    <div class="abs more" style="left:0;top:90px">MORE</div>
  </div>
  <div class="abs service" style="left:290px;top:18px">
    <div class="abs icon" role="img" aria-label="Social media icon"></div>
    <h3 class="abs">SOCIAL MEDIA</h3>
    <p class="abs">Fast track business success through the use of social media solutions and strategies.</p>
    <div class="abs more" style="left:72px;top:68px">MORE</div>
  </div>
  <div class="abs service" style="left:560px;top:18px">
    <div class="abs icon" role="img" aria-label="Web development icon"></div>
    <h3 class="abs">WEB DEVELOPMENT</h3>
    <p class="abs">Website solutions designed and developed to maximise your online business.</p>
    <div class="abs more" style="left:72px;top:68px">MORE</div>
  </div>
  <div class="abs service" style="left:20px;top:140px">
    <div class="abs icon" role="img" aria-label="E-commerce icon"></div>
    <h3 class="abs">E-COMMERCE</h3>
    <p class="abs">E-commerce solutions tailored to your business goals and objectives to help drive sales.</p>
    <div class="abs more" style="left:72px;top:80px">MORE</div>
  </div>
  <div class="abs service" style="left:290px;top:140px">
    <div class="abs icon" role="img" aria-label="Online business icon"></div>
    <h3 class="abs">ONLINE BUSINESS</h3>
    <p class="abs">Online specific business plans designed to help you take your idea to the next level.</p>
    <div class="abs more" style="left:72px;top:80px">MORE</div>
  </div>
  <div class="abs service" style="left:560px;top:140px">
    <div class="abs icon" role="img" aria-label="Online marketing icon"></div>
    <h3 class="abs">ONLINE MARKETING</h3>
    <p class="abs">Online marketing solutions developed to enhance your website and grow your business.</p>
    <div class="abs more" style="left:72px;top:80px">MORE</div>
  </div>
</section>

<section class="abs recent">
  <h2>Browse recent work</h2>
  <div class="abs strip">
    <div class="abs arrow l"></div>
    <div class="abs thumb" style="left:30px" role="img" aria-label="Website project preview"></div>
    <div class="abs thumb" style="left:156px" role="img" aria-label="Website project preview"></div>
    <div class="abs thumb" style="left:282px" role="img" aria-label="Website project preview"></div>
    <div class="abs thumb" style="left:408px" role="img" aria-label="Website project preview"></div>
    <div class="abs thumb" style="left:534px" role="img" aria-label="Website project preview"></div>
    <div class="abs thumb" style="left:660px" role="img" aria-label="Website project preview"></div>
    <div class="abs arrow r"></div>
  </div>
</section>

<section class="abs why">
  <h2>Why choose us</h2>
  <div class="abs body">
    <ul class="abs" style="left:0;top:10px">
      <li>Website solutions tailored to your business</li>
      <li>Cost-effective pricing to suit your budget</li>
      <li>Strategies to support your online presence</li>
      <li>Regular maintenance packages available</li>
    </ul>
    <ul class="abs" style="left:270px;top:10px">
      <li>Online business plans to promote growth</li>
      <li>SEO techniques incorporated into all solutions</li>
      <li>Online marketing options available</li>
      <li>Blogs and e-commerce solutions available</li>
    </ul>
    <div class="abs more-link">MORE &gt;&gt;</div>
  </div>
  <aside class="abs feed">
    <h3>Latest from Chatter</h3>
    <p>Lorem ipsum dolor sit amet, inermis patrioque te es, ut potent latine scripserit mei. <span class="time">Read more</span></p>
    <p>Lorem ipsum dolor sit amet, inermis patrioque te es, ut potent latine scripserit mei. <span class="time">Read more</span></p>
  </aside>
  <aside class="abs fbox">
    <div class="mark"></div>
    <div><div class="name">Brimvale Solutions</div><div class="on">WE ARE ON FRIENDBOOK</div></div>
  </aside>
</section>

<footer class="abs footer">
  <div class="abs col" style="left:30px">
    <h4>Quick links</h4>
    <div class="links">
      <span>Home</span><span>Blogs</span>
      <span>About</span><span>Social media</span>
      <span>Services</span><span>Web development</span>
      <span>Portfolio</span><span>E-commerce</span>
      <span>Contact</span><span>Online business</span>
      <span></span><span>Online marketing</span>
    </div>
  </div>
  <div class="abs col" style="left:320px;width:260px">
    <h4>Latest blog</h4>
    <p>Lorem ipsum dolor sit amet, inermis patrioque te es, ut potent latine scripserit mei.<br><span class="when">10 minutes ago</span></p>
    <p style="margin-top:6px">Lorem ipsum dolor sit amet, inermis patrioque te es, ut potent latine scripserit mei.<br><span class="when">10 minutes ago</span></p>
  </div>
  <div class="abs col" style="left:640px">
    <h4>Social media</h4>
    <div class="soc"><i></i>Friendbook</div>
    <div class="soc"><i></i>Chatter</div>
  </div>
</footer>
<div class="abs copy">Copyright © Brimvale Solutions. All rights reserved.</div>

</body>
</html>
```